Real Estate Agent needs business card design

We have logo designed already, want to have business card designed. Very interested in those smaller size business card as they look very trendy. Business name is called VORENDA REALTY

```html
<!DOCTYPE html>
<html lang="en">
<head>
<meta charset="utf-8">
<title>Vorenda Realty – Business Card</title>
<link href="https://fonts.googleapis.com/css2?family=Merriweather:wght@400;700&display=swap" rel="stylesheet">
<style>
  :root {
    --gold: #c9a46c;
    --gold-deep: #b88f55;
    --ink: #2b2b2b;
    --paper: #ffffff;
    --backdrop: #e9e6e1;
  }
  * { margin: 0; padding: 0; box-sizing: border-box; }
  html, body {
    width: 1200px; height: 880px; overflow: hidden;
    background: var(--backdrop);
    font-family: "Merriweather", Georgia, serif;
  }
  .canvas { position: relative; width: 1200px; height: 880px; }

  .card {
    position: absolute;
    width: 560px; height: 340px;
    border-radius: 22px;
    box-shadow: 0 10px 30px rgba(0,0,0,0.15);
    overflow: hidden;
  }

  /* Back of card */
  .card-back { left: 90px; top: 80px; background: var(--gold); }
  .card-back .pattern-area {
    position: absolute; inset: 0;
    background: linear-gradient(135deg, var(--gold) 0%, #c49d63 100%);
  }
  .card-back .brand-name {
    position: absolute; left: 0; right: 0; top: 128px;
    text-align: center; color: var(--paper);
    font-size: 40px; font-weight: 700; letter-spacing: 4px;
  }
  .card-back .web {
    position: absolute; left: 0; right: 0; top: 200px;
    text-align: center; color: var(--paper);
    font-size: 15px; letter-spacing: 0.5px;
  }

  /* Front of card */
  .card-front { left: 550px; top: 460px; background: var(--paper); }
  .badge {
    position: absolute; left: 40px; top: 95px;
    width: 150px; height: 150px; border-radius: 50%;
    background: var(--gold);
    display: flex; align-items: center; justify-content: center;
  }
  .badge .badge-name {
    color: var(--paper); font-size: 13px; letter-spacing: 1.5px;
    text-align: center; line-height: 1.5;
  }
  .divider {
    position: absolute; left: 232px; top: 70px;
    width: 1px; height: 200px; background: var(--gold);
  }
  .details { position: absolute; left: 262px; top: 78px; color: var(--ink); }
  .agent-name { color: var(--gold-deep); font-size: 24px; font-weight: 700; line-height: 1.1; }
  .agent-role { font-size: 12px; margin-top: 4px; }
  .contact { margin-top: 22px; list-style: none; font-size: 13px; }
  .contact li { display: flex; align-items: center; gap: 8px; margin-bottom: 6px; }
  .contact svg { width: 16px; height: 16px; flex: none; }
  .address { margin-top: 14px; font-size: 13px; line-height: 1.55; }
</style>
</head>
<body>
<main class="canvas">

  <section class="card card-back">
    <div class="pattern-area" role="img" aria-label="Faint repeating monogram pattern in tonal gold"></div>
    <div class="brand-name">VORENDA REALTY</div>
    <div class="web">www.vorendarealty.com.au</div>
  </section>

  <section class="card card-front">
    <div class="badge">
      <div class="badge-name">VORENDA<br>REALTY</div>
    </div>
    <div class="divider"></div>
    <div class="details">
      <div class="agent-name">Elena Marsh</div>
      <div class="agent-role">Senior Property Consultant</div>
      <ul class="contact">
        <li>
          <svg viewBox="0 0 16 16" aria-hidden="true">
            <circle cx="8" cy="8" r="7.5" fill="var(--gold)"/>
            <path d="M5.2 4.2l1.4 0 .7 1.8-.9.7c.5 1 1.2 1.7 2.2 2.2l.7-.9 1.8.7v1.4c0 .4-.3.7-.7.7C7.3 11.3 4.7 8.7 4.5 4.9c0-.4.3-.7.7-.7z" fill="#fff"/>
          </svg>
          0412 555 019
        </li>
        <li>
          <svg viewBox="0 0 16 16" aria-hidden="true">
            <circle cx="8" cy="8" r="7.5" fill="var(--gold)"/>
            <circle cx="8" cy="8" r="4" fill="none" stroke="#fff" stroke-width="0.9"/>
            <ellipse cx="8" cy="8" rx="1.8" ry="4" fill="none" stroke="#fff" stroke-width="0.9"/>
            <line x1="4" y1="8" x2="12" y2="8" stroke="#fff" stroke-width="0.9"/>
          </svg>
          www.vorendarealty.com.au
        </li>
      </ul>
      <div class="address">7C, 48 Harbour Road<br>Kelvin Bay, NSW 2099</div>
    </div>
  </section>

</main>
</body>
</html>
```